Business Card & Logo Design - Hedge Fund

We need a business card and logo design for a hedge fund. The hedge fund is named Morvane Holdings LLC. Morvane Holdings was created by finance professors and the strategy is based academic research that looks for patterns in stock prices. The design should look conservative, solid, strong. We favor a classic style - nothing flashy. The logo can relate to the name Morvane Holdings, or it could involve a symbol design that connotes "science" . We are open to ideas. We do not want alot of colors - but if any, color - blue is preferred. The font that seems to look best for the name (Morvane Holdings) is arial black. We are open to ideas. Most important - we want to see a mock up of an actual business card with the logo concept embedded. The business card should include space for : company name, individual name, position title, cell phone, address. We hope to have this work done by Sept. 8.

Target Market(s)

We will be meeting with and giving the business card to institutions and high net worth individuals.

Industry/Entity Type

Investment Advisory

Contact Information for Business Card

Company name - Morvane Holdings LLC
Individual name - Peter Vosk
Title - Portfolio Manager
Cell - (482) 555-0137
Address - 2750 Birchwell Lane, Suite 300, Atlanta GA 30327

Font styles to use
Other font styles liked:
• Arial

Colors
3277b5
0255a3
85acd3
cedeed
fdf9cf
d9d9d9
e6e6e6
f04a50
6b449b

Requirements
Must have
• Must have card details that are sited above.
• We would like a logo related to the name (Morvane Holdings) or concept of the fund.
Nice to have
• We want conservative / understated / clean crisp look.
• If any colors - we prefer conservative appearance - blue / gray.
• I have enclosed an example of a card style that looks attractive - please do not exactly copy this card. This is not our company or logo. I feel the layout is attractive - just as an example
Should not have
• Avoid too much color.
• I have selected some preferred colors. Please do not use all of the colors - I have selected a few that might work - but I am not sure. We are open to your ideas so please do not feel the need to use all or any of these.

```html
<!DOCTYPE html>
<html lang="en">
<head>
<meta charset="utf-8">
<title>Morvane Holdings LLC – Business Card</title>
<link href="https://fonts.googleapis.com/css2?family=Archivo+Black&family=Work+Sans:wght@400;500;700&display=swap" rel="stylesheet">
<style>
  :root {
    --navy: #29235f;
    --navy-deep: #221d52;
    --white: #ffffff;
    --grey: #6e6e70;
    --grey-light: #d9d9d9;
    --ink: #3a3a44;
    --stage: #262629;
  }
  * { box-sizing: border-box; margin: 0; padding: 0; }
  html, body { width: 1200px; height: 738px; overflow: hidden; }
  body {
    background: var(--stage);
    font-family: "Work Sans", Arial, sans-serif;
    position: relative;
  }
  .card {
    position: absolute;
    top: 214px;
    width: 540px;
    height: 309px;
    overflow: hidden;
    box-shadow: 0 10px 30px rgba(0,0,0,.45);
  }
  .card--back { left: 40px; background: var(--navy); }
  .card--front { left: 620px; background: var(--white); }

  .brand {
    display: flex;
    align-items: center;
    gap: 10px;
    font-family: "Archivo Black", "Arial Black", sans-serif;
    white-space: nowrap;
  }
  .brand__dot { border-radius: 50%; flex: none; }
  .card--back .brand {
    position: absolute; left: 0; right: 0; top: 132px;
    justify-content: center;
    color: var(--white);
    font-size: 27px;
  }
  .card--back .brand__dot { width: 34px; height: 34px; border: 4px solid var(--white); }

  .card--front .brand {
    position: absolute; left: 30px; top: 138px;
    color: var(--navy);
    font-size: 14.5px;
    gap: 8px;
  }
  .card--front .brand__dot { width: 20px; height: 20px; border: 3px solid var(--navy); }

  .divider {
    position: absolute; left: 262px; top: 62px;
    width: 1.5px; height: 128px;
    background: var(--navy);
  }
  .details { position: absolute; left: 284px; top: 58px; color: var(--ink); }
  .details__name {
    font-weight: 700; font-size: 21px; letter-spacing: 2px;
    color: var(--navy); text-transform: uppercase; line-height: 1;
  }
  .details__title { font-size: 12px; color: var(--grey); margin-top: 4px; letter-spacing: .4px; }
  .details__address { font-size: 12.5px; line-height: 1.35; margin-top: 14px; letter-spacing: .3px; }
  .contact { list-style: none; margin-top: 12px; font-size: 12.5px; letter-spacing: .3px; }
  .contact li { display: flex; align-items: center; gap: 8px; line-height: 1.3; }
  .contact svg { width: 10px; height: 10px; flex: none; fill: var(--navy); }
  .contact .contact__web-domain { color: var(--navy); }

  .wave { position: absolute; left: 0; bottom: 0; width: 540px; height: 120px; }
</style>
</head>
<body>
  <section class="card card--back" aria-label="Card back">
    <div class="brand"><span class="brand__dot"></span><span>Morvane Holdings LLC</span></div>
  </section>

  <section class="card card--front" aria-label="Card front">
    <div class="brand"><span class="brand__dot"></span><span>Morvane Holdings LLC</span></div>
    <div class="divider"></div>
    <div class="details">
      <p class="details__name">Peter Vosk</p>
      <p class="details__title">Portfolio Manager</p>
      <p class="details__address">2750 Birchwell Lane,<br>Suite 300, Atlanta GA 30327</p>
      <ul class="contact">
        <li><svg viewBox="0 0 10 10"><path d="M2 0h2l1 2.5-1.3 1a5 5 0 0 0 2.8 2.8l1-1.3L10 6v2c0 1-1 2-2 2A8 8 0 0 1 0 2c0-1 1-2 2-2z"/></svg><span>(482) 555-0137</span></li>
        <li><svg viewBox="0 0 10 10"><path d="M0 2h10v6H0zM1 3v.3l4 2.5 4-2.5V3zm0 1.5V7h8V4.5L5 7z"/></svg><span>info@morvaneholdings.com</span></li>
        <li><svg viewBox="0 0 10 10"><path d="M5 0a5 5 0 1 0 0 10A5 5 0 0 0 5 0zm0 1.2c.6.6 1 1.7 1.1 3.2H3.9C4 2.9 4.4 1.8 5 1.2zM1.3 4.4a3.8 3.8 0 0 1 1.9-2.8c-.3.8-.5 1.7-.5 2.8zm0 1.2h1.4c0 1.1.2 2 .5 2.8a3.8 3.8 0 0 1-1.9-2.8zM5 8.8c-.6-.6-1-1.7-1.1-3.2h2.2C6 7.1 5.6 8.2 5 8.8zm1.8-.4c.3-.8.5-1.7.5-2.8h1.4a3.8 3.8 0 0 1-1.9 2.8zm.5-4c0-1.1-.2-2-.5-2.8a3.8 3.8 0 0 1 1.9 2.8z"/></svg><span>www.<span class="contact__web-domain">morvaneholdings.com</span></span></li>
      </ul>
    </div>
    <svg class="wave" viewBox="0 0 540 120" preserveAspectRatio="none" aria-hidden="true">
      <path d="M0 94 C140 112 260 64 360 36 C430 16 490 10 540 14 L540 120 L0 120 Z" fill="var(--grey)"/>
      <path d="M0 98 C140 116 262 70 362 42 C432 22 490 16 540 20" fill="none" stroke="var(--white)" stroke-width="3"/>
      <path d="M0 102 C140 120 264 76 364 48 C434 28 492 22 540 26 L540 120 L0 120 Z" fill="var(--navy)"/>
    </svg>
  </section>
</body>
</html>
```